Need to make a work slip for trucking company.

I need a form to fill out for my truck drivers to get signed on delivery. It is for a trucking company and this form will be for each machine equipment move. I have included my old sheet which I need Updated. Its going on a 9.5 inch by 8.5 inch sheet of paper. It should have room for the day, date, customer name, ordered by, P.O. Number, Project Number, Driver, Truck/Trailer, Tolls (needs more room then my old sheet need a few lines under each other for each toll during the machine move), Permits, some room for other information, Loads, Hours, and 2 lines for a Signature and Print Line.
Updates

Need to also include a Pickup Address and a Deliver Address with lines to write in. Also I need to add a Print Line (and labeled Print) for whoever is signing the ticket.

Requirements
Must have
• My new company name and Logo. I have included my new Logo. It must be easy to ready. Must include my company colors. (Concrete Gray, and Neon Blue)

```html
<!DOCTYPE html>
<html lang="en">
<head>
<meta charset="utf-8">
<title>Work Slip – Harbor Line Transport</title>
<link href="https://fonts.googleapis.com/css2?family=Open+Sans:wght@400;600;700&display=swap" rel="stylesheet">
<style>
  :root{
    --page-bg:#ebebeb;
    --sheet-bg:#ffffff;
    --frame-blue:#1a6fe0;
    --brand-blue:#1266ae;
    --header-light:#f5f5f5;
    --header-gray:#e8e8e8;
    --ticket-red:#c8393b;
    --ink:#222222;
    --ink-soft:#444444;
    --rule:#b3b3b3;
  }
  *{margin:0;padding:0;box-sizing:border-box}
  html,body{width:1200px;height:1082px;overflow:hidden;background:var(--page-bg)}
  body{font-family:"Open Sans",Arial,sans-serif;color:var(--ink);position:relative}
  .slip{position:absolute;left:41px;top:41px;width:1118px;height:1000px;background:var(--sheet-bg);border:3px solid var(--frame-blue)}
  .abs{position:absolute}
  .header-bg{position:absolute;left:49px;top:49px;width:1102px;height:172px}
  .ticket-no{left:68px;top:70px;font-size:33px;line-height:40px;color:var(--ticket-red)}
  .days{left:71px;top:137px;font-size:18px;line-height:24px;font-weight:700;color:#333;word-spacing:8px;letter-spacing:1px}
  .ampm{left:71px;top:178px;font-size:18px;line-height:24px;font-weight:700;color:#333}
  .brand{left:400px;width:400px;top:72px;text-align:center;font-size:22px;line-height:30px;font-weight:700;color:var(--brand-blue)}
  .contact{left:350px;width:500px;text-align:center;font-size:16px;line-height:22px;color:var(--ink-soft)}
  .date-label{left:948px;top:137px;font-size:18px;line-height:24px;font-weight:700;color:#fff}
  .date-rule{left:948px;top:195px;width:182px;height:2px;background:#fff}
  .label{font-size:18px;line-height:24px;color:var(--ink)}
  .label-left{left:71px}
  .label-right{left:622px}
  .rule{height:1.5px;background:var(--rule)}
  .rule-left{left:186px;width:392px}
  .rule-right{left:622px;width:507px}
</style>
</head>
<body>
  <div class="slip"></div>

  <svg class="header-bg" viewBox="0 0 1102 172" aria-hidden="true">
    <rect width="1102" height="172" fill="var(--header-light)"/>
    <polygon points="0,0 360,0 262,172 0,172" fill="var(--header-gray)"/>
    <polygon points="857,0 1102,0 1102,172 759,172" fill="var(--brand-blue)"/>
  </svg>

  <header>
    <div class="abs ticket-no">19234</div>
    <div class="abs days">M T W T F S S</div>
    <div class="abs ampm">A.M. &nbsp;/&nbsp; P.M.</div>

    <div class="abs brand">Harbor Line Transport</div>
    <div class="abs contact" style="top:139px">Harbor Point, New York 11999</div>
    <div class="abs contact" style="top:178px">Phone (555) 014-3000 &nbsp;&nbsp;•&nbsp;&nbsp; Fax (555) 014-3009</div>

    <div class="abs date-label">DATE</div>
    <div class="abs date-rule"></div>
  </header>

  <section class="job-details">
    <div class="abs label label-left" style="top:259px">Customer</div>
    <div class="abs label label-left" style="top:303px">Ordered By</div>
    <div class="abs label label-left" style="top:347px">P.O. No.v.</div>
    <div class="abs label label-left" style="top:391px">Project No.</div>
    <div class="abs label label-left" style="top:435px">Driver</div>
    <div class="abs label label-left" style="top:479px">Tr.Eq.</div>
    <div class="abs label label-left" style="top:523px">L / W / H</div>
    <div class="abs label label-left" style="top:567px">Tolls</div>
    <div class="abs label label-left" style="top:743px">Permit(s)</div>
    <div class="abs label label-left" style="top:831px">Other</div>
    <div class="abs label label-left" style="top:919px">Loads</div>
    <div class="abs label label-left" style="top:963px">Hours</div>

    <div class="abs rule rule-left" style="top:278px"></div>
    <div class="abs rule rule-left" style="top:322px"></div>
    <div class="abs rule rule-left" style="top:366px"></div>
    <div class="abs rule rule-left" style="top:410px"></div>
    <div class="abs rule rule-left" style="top:454px"></div>
    <div class="abs rule rule-left" style="top:498px"></div>
    <div class="abs rule rule-left" style="top:542px"></div>
    <div class="abs rule rule-left" style="top:586px"></div>
    <div class="abs rule rule-left" style="top:630px"></div>
    <div class="abs rule rule-left" style="top:674px"></div>
    <div class="abs rule rule-left" style="top:718px"></div>
    <div class="abs rule rule-left" style="top:762px"></div>
    <div class="abs rule rule-left" style="top:806px"></div>
    <div class="abs rule rule-left" style="top:850px"></div>
    <div class="abs rule rule-left" style="top:894px"></div>
    <div class="abs rule rule-left" style="top:938px"></div>
    <div class="abs rule rule-left" style="top:982px"></div>
  </section>

  <section class="move-details">
    <div class="abs label label-right" style="top:259px">F/B * L/B * LD STR/TRL * BM/TK * DUMP TK</div>
    <div class="abs label label-right" style="top:292px">ROLL BACK * ROLL OFF</div>

    <div class="abs label label-right" style="top:435px">Pickup Address</div>
    <div class="abs rule rule-right" style="top:498px"></div>
    <div class="abs rule rule-right" style="top:542px"></div>

    <div class="abs label label-right" style="top:567px">Delivery Address</div>
    <div class="abs rule rule-right" style="top:630px"></div>
    <div class="abs rule rule-right" style="top:674px"></div>

    <div class="abs label label-right" style="top:743px">Signature</div>
    <div class="abs rule rule-right" style="top:806px"></div>
    <div class="abs rule rule-right" style="top:850px"></div>

    <div class="abs label label-right" style="top:875px">Print</div>
    <div class="abs rule rule-right" style="top:938px"></div>
    <div class="abs rule rule-right" style="top:982px"></div>
  </section>
</body>
</html>
```